Business card for Full Stable Care Vandorpe

I would like to have me designed an professional business card with my existing logo for my company called : full stable care vandorpe gcv.
I prefer a two sided business card with on the back side only the horses head and the website : fscvandorpe-example.eu
Only one colour shouldbe all right.
The logo must appear in a nic professional way on the business card.

Other suggestion are welcome.

All copy wrights must be released by the designer after we have selected a final design.

Target Market(s)

Equestrian businesses

Industry/Entity Type

Business

Contact Information for Business Card

Laurent Vandorpe
Title: zaakvoerder
Full Stable Care Vandorpe GCV
Molkenweg 47
B - 3195 Lindenvelde
België
Phone: + 32 491 68 27 04
Mail: laurent@fscvandorpe-example.eu

Font styles to use
Serif

Requirements
Must have
• My own logo
• See attached files
• Website: fscvandorpe-example.eu

```html
<!DOCTYPE html>
<html lang="nl">
<head>
<meta charset="utf-8">
<title>Full Stable Care Vandorpe – Business Card</title>
<link href="https://fonts.googleapis.com/css2?family=Jost:wght@400;500&display=swap" rel="stylesheet">
<style>
  :root {
    --ink: #333133;
    --text: #111111;
    --paper: #ffffff;
    --backdrop: #d9d9d9;
    --rule: #6d6b6d;
  }
  * { margin: 0; padding: 0; box-sizing: border-box; }
  html, body { width: 1200px; height: 1200px; overflow: hidden; }
  body {
    background: var(--backdrop);
    font-family: "Jost", sans-serif;
    color: var(--text);
    position: relative;
  }
  .card {
    position: absolute;
    left: 220px;
    width: 760px;
    height: 447px;
    background: var(--paper);
    box-shadow: 0 6px 18px rgba(0,0,0,0.18);
    overflow: hidden;
  }
  /* Front side */
  .card--front { top: 110px; display: flex; flex-direction: column; }
  .band { background: var(--ink); height: 124px; }
  .logo-band {
    flex: 1;
    display: flex;
    flex-direction: column;
    align-items: center;
    justify-content: center;
    gap: 18px;
  }
  .wordmark {
    display: flex;
    align-items: center;
    gap: 16px;
    font-size: 40px;
    font-weight: 500;
    color: var(--text);
  }
  .wordmark__dot {
    width: 44px; height: 44px;
    border-radius: 50%;
    background: var(--text);
  }
  .website {
    font-size: 16px;
    font-weight: 500;
    letter-spacing: 4px;
  }
  /* Back side */
  .card--back { top: 643px; }
  .holder { position: absolute; left: 70px; top: 120px; }
  .holder__name {
    font-size: 60px;
    font-weight: 500;
    line-height: 0.95;
  }
  .holder__title {
    font-size: 13px;
    letter-spacing: 4px;
    margin-top: 8px;
    margin-left: 80px;
  }
  .company {
    position: absolute;
    left: 130px;
    top: 300px;
    font-size: 18px;
    font-weight: 500;
    letter-spacing: 4px;
  }
  .contact {
    position: absolute;
    left: 440px;
    right: 0;
    top: 120px;
    background: var(--ink);
    color: var(--paper);
    padding: 14px 22px 14px 16px;
    font-size: 15px;
    line-height: 1.2;
  }
  .contact__row {
    display: flex;
    gap: 14px;
    align-items: flex-start;
    padding: 9px 0;
  }
  .contact__row + .contact__row { border-top: 1px solid var(--rule); }
  .contact__row svg { flex: none; width: 18px; height: 18px; margin-top: 1px; }
</style>
</head>
<body>

<section class="card card--front">
  <div class="band"></div>
  <div class="logo-band">
    <div class="wordmark"><span class="wordmark__dot"></span>Full Stable Care Vandorpe</div>
    <div class="website">www.fscvandorpe-example.eu</div>
  </div>
  <div class="band"></div>
</section>

<section class="card card--back">
  <div class="holder">
    <h1 class="holder__name">Laurent<br>Vandorpe</h1>
    <p class="holder__title">zaakvoerder</p>
  </div>
  <p class="company">Full Stable Care Vandorpe GCV</p>

  <div class="contact">
    <div class="contact__row">
      <svg viewBox="0 0 24 24" aria-hidden="true"><path fill="#fff" d="M6.6 10.8a15 15 0 0 0 6.6 6.6l2.2-2.2c.3-.3.7-.4 1-.2 1.1.4 2.3.6 3.6.6.6 0 1 .4 1 1V20c0 .6-.4 1-1 1A17 17 0 0 1 3 4c0-.6.4-1 1-1h3.5c.6 0 1 .4 1 1 0 1.3.2 2.5.6 3.6.1.3 0 .7-.2 1z"/></svg>
      <span>+ 32 491 68 27 04</span>
    </div>
    <div class="contact__row">
      <svg viewBox="0 0 24 24" aria-hidden="true" fill="none" stroke="#fff" stroke-width="1.6"><circle cx="12" cy="12" r="9"/><ellipse cx="12" cy="12" rx="4" ry="9"/><path d="M3 12h18M5 7h14M5 17h14"/></svg>
      <span>laurent@fscvandorpe-example.eu<br>www.fscvandorpe-example.eu</span>
    </div>
    <div class="contact__row">
      <svg viewBox="0 0 24 24" aria-hidden="true"><path fill="#fff" d="M12 2a7 7 0 0 0-7 7c0 5 7 13 7 13s7-8 7-13a7 7 0 0 0-7-7zm0 9.5A2.5 2.5 0 1 1 12 6.5a2.5 2.5 0 0 1 0 5z"/></svg>
      <span>Molkenweg 47 B,<br>3195 Lindenvelde, België</span>
    </div>
  </div>
</section>

</body>
</html>
```